Benefit Card for new Customers - LUMIRO

We are planning our offline referral marketing programm. So we need a benefit card for new customers. We are a company that provides innovative and highly competent private tutoring for our customers. We are LUMIRO (www.lumiro-lernhilfe.ch) and are located in Bern (Switzerland). Our customers are schoolkids (and their parents), apprentices and students. Therefore we designed our corporate design for this target groups. Our corporate design is colourful (we use especially our corporate colours) and has as little edges as possible. As an illustration take a look at our website www.lumiro-lernhilfe.ch where we tried to realize our corporate identity as suitable as possible.
We would like to see designs that use our corporate colours (green, blue and tourquois might be inviting colours). The final design should be inviting for new customers, highly professional and not too overloaded.

Dimensions of the card: 148 x 105 mm (millimeter) --> A6 Format
Font: Lato

Upload Files:
- Corporate colour codes
- rough draft of the benefit card
- text and wording document
- Logo

Target Market(s)

Schoolkids (and their parents), apprentices, students

Industry/Entity Type

Education

Requirements
Must have
• Clean Design, Font: Lato, right Dimension as mentioned in the despriction,
Should not have
• Edges

```html
<!DOCTYPE html>
<html lang="de">
<head>
<meta charset="utf-8">
<title>Vorteils-Pass – LUMIRO</title>
<link href="https://fonts.googleapis.com/css2?family=Lato:wght@400;700;900&display=swap" rel="stylesheet">
<style>
  :root {
    --brand-green: #97cb5a;
    --brand-teal: #63c3a3;
    --ink: #111111;
    --logo-ink: #3a3d44;
    --bg-top: #ffffff;
    --bg-bottom: #d3e9b8;
  }
  * { margin: 0; padding: 0; box-sizing: border-box; }
  html, body { width: 1200px; height: 852px; overflow: hidden; }
  body { font-family: "Lato", sans-serif; color: var(--ink); }
  .card {
    position: relative;
    width: 1200px; height: 852px;
    background: linear-gradient(180deg, var(--bg-top) 0%, #eef6e4 40%, var(--bg-bottom) 100%);
    overflow: hidden;
  }
  .bands { position: absolute; inset: 0; }
  .title {
    position: absolute; left: 50px; top: 78px;
    font-size: 86px; font-weight: 900; letter-spacing: -1px;
    color: var(--brand-green); line-height: 1;
  }
  .lead {
    position: absolute; left: 41px; top: 214px;
    font-size: 36px; font-weight: 700; line-height: 52px;
  }
  .brand-seal {
    position: absolute; left: 848px; top: 59px;
    width: 290px; height: 290px; border-radius: 50%;
    background: #fff; border: 9px solid var(--brand-green);
    display: flex; align-items: center; justify-content: center;
  }
  .brand-seal .brand-name {
    font-size: 44px; font-weight: 700; letter-spacing: 6px; color: var(--logo-ink);
  }
  .row { position: absolute; font-size: 29px; line-height: 1; white-space: nowrap; }
  .fill-line { position: absolute; height: 0; border-bottom: 2px solid var(--ink); }
  .checkbox {
    position: absolute; width: 31px; height: 31px;
    border: 2.5px solid var(--brand-teal); border-radius: 2px;
  }
  .tick { position: absolute; left: 920px; top: 468px; }
  .contact {
    position: absolute; right: 42px; top: 660px; text-align: right;
    font-weight: 700; white-space: nowrap;
  }
  .contact .phone { font-size: 29px; line-height: 1; margin-bottom: 14px; }
  .contact .web { font-size: 25px; line-height: 1; margin-bottom: 16px; }
  .contact .sep { margin: 0 14px; }
</style>
</head>
<body>
<main class="card">
  <svg class="bands" width="1200" height="852" viewBox="0 0 1200 852" aria-hidden="true">
    <polygon points="0,0 1200,0 1200,17 822,17 797,55 0,55" fill="var(--brand-green)"/>
    <polygon points="0,852 0,830 489,830 523,793 1200,793 1200,852" fill="var(--brand-green)"/>
  </svg>

  <h1 class="title">Dein Vorteils-Pass</h1>
  <p class="lead">Mit diesem Vorteils-Pass schenken wir Dir<br>eine Unterrichtslektion.</p>

  <div class="brand-seal"><span class="brand-name">LUMIRO</span></div>

  <div class="row" style="left:41px; top:386px;">Empfehler:</div>
  <div class="fill-line" style="left:199px; width:279px; top:413px;"></div>
  <div class="row" style="left:487px; top:386px;">erhält Gratislektion</div>
  <div class="checkbox" style="left:769px; top:383px;"></div>
  <div class="row" style="left:828px; top:386px;">oder Kinogutschein</div>
  <div class="checkbox" style="left:1112px; top:383px;"></div>

  <div class="row" style="left:41px; top:484px;">Freund:</div>
  <div class="fill-line" style="left:154px; width:324px; top:511px;"></div>
  <div class="row" style="left:487px; top:484px;">erhält die vierte Lektion gratis</div>
  <svg class="tick" width="50" height="50" viewBox="0 0 50 50" aria-hidden="true">
    <circle cx="25" cy="25" r="22.5" fill="none" stroke="var(--brand-teal)" stroke-width="3"/>
    <path d="M15 26 L22 33 L37 16" fill="none" stroke="var(--brand-teal)" stroke-width="3.5" stroke-linecap="round" stroke-linejoin="round"/>
  </svg>

  <div class="row" style="left:41px; top:590px;">Melde Dich bei uns und lass Dich kostenlos und unverbindlich beraten.</div>

  <div class="contact">
    <div class="phone">031 555 18 62</div>
    <div class="web">www.lumiro-lernhilfe.ch<span class="sep">•</span>hallo@lumiro-lernhilfe.ch</div>
    <div class="web">weitere Infos: www.lumiro-lernhilfe.ch/freundschaft/</div>
  </div>

  <div class="row" style="left:41px; top:770px;">Vorteils-Pass-Nr.</div>
  <div class="fill-line" style="left:281px; width:197px; top:796px;"></div>
</main>
</body>
</html>
```